Simple and clean

We need a business card design for a new company called Estate Lantern. It is a search engine to find current properties for sale or rent in New Zealand market.
We have already a colour scheme that we would like people to use.
Light brown: #D4CCB0
Light green: #D6E4D4
Green: #669966
Black/White
It is OK to divert from this colour scheme slightly as long as there is a green component to the business card.
Final design should be clean, simple and should communicate the nature of the business.
Target Market(s)
- First home buyers
- Real estate agents
- People seeking rentals
Industry/Entity Type
Business
Requirements
Must have
- Use those or similar colours.
Light brown: #D4CCB0
Light green: #D6E4D4
Green: #669966
Black/White

```html
<!DOCTYPE html>
<html lang="en">
<head>
<meta charset="utf-8">
<title>Estate Lantern – Business Card</title>
<link rel="stylesheet" href="https://fonts.googleapis.com/css2?family=Roboto:wght@400;700&display=swap">
<style>
  :root {
    --page-bg: #f1f1ee;
    --card-sage: #a9b898;
    --stripe-white: #ffffff;
    --stripe-mint: #c9dcc4;
    --ink-green: #3d6937;
    --label-green: #5a7152;
    --mark-green: #669966;
  }
  html, body {
    margin: 0;
    width: 1200px;
    height: 2900px;
    overflow: hidden;
    background: var(--page-bg);
    font-family: "Roboto", Arial, sans-serif;
  }
  .canvas {
    position: relative;
    width: 1200px;
    height: 2900px;
  }
  .business-card {
    position: absolute;
    left: 75px;
    top: 1150px;
    width: 1050px;
    height: 600px;
    background: var(--card-sage);
    overflow: hidden;
    box-shadow: 0 10px 30px rgba(0,0,0,0.18);
  }
  .stripe {
    position: absolute;
    top: 0;
    height: 100%;
    background: linear-gradient(to bottom,
      var(--stripe-white) 0%,
      var(--stripe-white) 25%,
      var(--stripe-mint) 50%,
      var(--stripe-white) 75%,
      var(--stripe-white) 100%);
  }
  .stripe--left { left: 150px; width: 85px; }
  .stripe--right { left: 815px; width: 85px; }
  .brand {
    position: absolute;
    left: 660px;
    top: 70px;
    display: flex;
    align-items: center;
    gap: 14px;
  }
  .brand__dot {
    width: 40px;
    height: 40px;
    border-radius: 50%;
    background: var(--mark-green);
    flex: none;
  }
  .brand__name {
    font-size: 34px;
    font-weight: 700;
    color: var(--ink-green);
    white-space: nowrap;
    line-height: 1;
  }
  .holder {
    position: absolute;
    left: 300px;
    top: 190px;
    color: var(--ink-green);
  }
  .holder__name {
    margin: 0;
    font-size: 46px;
    font-weight: 700;
    line-height: 1;
  }
  .holder__role {
    margin: 6px 0 0;
    font-size: 30px;
    font-weight: 400;
    letter-spacing: 0.5px;
    line-height: 1;
  }
  .contact {
    position: absolute;
    right: 290px;
    top: 262px;
    text-align: right;
    margin: 0;
  }
  .contact dt {
    font-size: 25px;
    font-weight: 400;
    color: var(--label-green);
    line-height: 1.1;
    letter-spacing: 0.5px;
  }
  .contact dd {
    margin: 0 0 10px;
    font-size: 26px;
    font-weight: 700;
    color: var(--ink-green);
    line-height: 1.15;
  }
  .website {
    position: absolute;
    right: 270px;
    top: 470px;
    margin: 0;
    font-size: 44px;
    font-weight: 700;
    color: var(--ink-green);
    white-space: nowrap;
  }
</style>
</head>
<body>
<main class="canvas">
  <article class="business-card">
    <div class="stripe stripe--left"></div>
    <div class="stripe stripe--right"></div>

    <div class="brand">
      <span class="brand__dot" aria-hidden="true"></span>
      <span class="brand__name">Estate Lantern</span>
    </div>

    <header class="holder">
      <h1 class="holder__name">Mara Whitcombe</h1>
      <p class="holder__role">DIRECTOR</p>
    </header>

    <dl class="contact">
      <dt>PHONE</dt>
      <dd>021-555-0142</dd>
      <dt>EMAIL</dt>
      <dd>mara@estatelantern.co.nz</dd>
      <dt>WEBSITE</dt>
    </dl>
    <p class="website">www.estatelantern.co.nz</p>
  </article>
</main>
</body>
</html>
```